BRIGHTPATH TV SALES PITCH TEMPLATE

We need a cover sheet and template for a Power Point presentation we are giving. Our new cable network is all about self improvement and professional development. This Power Point will include information about the business ad programs we will offer. It needs to be in color and lend itself to a digital media look. The presentation will probably be about 10 to 15 slides. We have attached one that we did a few years ago that I did not think was strong enough. You can call me at US 812-356-2094

Target Market(s)

Media companies

Industry/Entity Type

Television Station

Requirements
Must have
• Ability to easily lay in text and edit with single, elegant font. Also, we would like to add images.
Nice to have
• Must look professional and incorporate our logo, but also be cutting edge

```html
<!DOCTYPE html>
<html lang="en">
<head>
<meta charset="utf-8">
<title>BRIGHTPATH TV — Presentation Template</title>
<link href="https://fonts.googleapis.com/css2?family=Barlow+Semi+Condensed:wght@300;400;600&display=swap" rel="stylesheet">
<style>
  :root {
    --stage: #ababab;
    --ink-dark: #1f1d1e;
    --paper: #ffffff;
    --accent-red: #c4161c;
    --title-brown: #4a3a22;
    --toc-brown: #7a5a2a;
    --body-ink: #2a2a2a;
    --muted: #8a8a8a;
    --contact-dot: #d79a3a;
    --font: "Barlow Semi Condensed", "Arial Narrow", sans-serif;
  }
  * { box-sizing: border-box; margin: 0; padding: 0; }
  html, body { width: 1200px; height: 1200px; overflow: hidden; }
  body { background: var(--stage); font-family: var(--font); position: relative; }

  .slide {
    position: absolute; width: 534px; height: 400px;
    background: var(--paper); overflow: hidden;
    box-shadow: 6px 8px 10px rgba(0,0,0,0.35);
  }
  .slide--cover   { left: 56px;  top: 170px; }
  .slide--contents{ left: 610px; top: 170px; }
  .slide--body    { left: 56px;  top: 592px; }
  .slide--closing { left: 610px; top: 592px; }

  .sidebar { position: absolute; left: 0; top: 0; bottom: 0; background: var(--ink-dark); }
  .sidebar--narrow { width: 45px; }
  .sidebar--wide { width: 190px; }
  .sidebar--half { width: 297px; }
  .sidebar-mark {
    position: absolute; left: 14px; bottom: 22px; width: 17px; height: 17px;
    background: var(--accent-red);
  }

  .wordmark {
    position: absolute; color: var(--paper); font-weight: 600;
    letter-spacing: 0.5px; white-space: nowrap;
  }
  .slide--cover .wordmark { left: 24px; top: 340px; font-size: 21px; }
  .slide--closing .wordmark { left: 50px; top: 338px; font-size: 34px; }

  .cover-title {
    position: absolute; left: 210px; top: 80px;
    color: var(--accent-red); font-size: 34px; font-weight: 400; letter-spacing: 0.5px;
  }
  .cover-subtitle {
    position: absolute; left: 210px; top: 136px; width: 310px;
    color: var(--body-ink); font-size: 17.5px; font-weight: 400; line-height: 18px;
  }

  .slide-title {
    position: absolute; left: 69px; top: 29px;
    color: var(--title-brown); font-size: 22px; font-weight: 400; letter-spacing: 0.3px;
  }
  .slide-subtitle {
    position: absolute; left: 69px; top: 58px;
    color: var(--title-brown); font-size: 17.5px; font-weight: 400;
  }

  .toc { position: absolute; left: 69px; top: 75px; width: 437px; list-style: none; }
  .toc li { display: flex; align-items: baseline; height: 17.6px; white-space: nowrap; }
  .toc .entry { color: var(--toc-brown); font-size: 9.5px; }
  .toc .leader { flex: 1; border-bottom: 1px dotted var(--toc-brown); margin: 0 2px 0 3px; height: 1px; align-self: center; transform: translateY(3px); min-width: 10px; }
  .toc .page { width: 33px; text-align: right; color: var(--title-brown); font-size: 9.5px; }
  .toc li.sub .entry { font-size: 7.5px; padding-left: 27px; color: #6b5a40; }

  .columns {
    position: absolute; left: 67px; top: 88px; width: 434px; height: 270px;
    column-count: 2; column-gap: 13px; column-fill: auto;
    color: var(--body-ink); font-size: 8px; font-weight: 300; line-height: 11.9px; text-align: justify;
    hyphens: auto;
  }
  .columns p { margin-bottom: 11.9px; }
  .page-number { position: absolute; left: 492px; top: 368px; font-size: 14px; color: var(--body-ink); }

  .contact { position: absolute; left: 322px; top: 356px; list-style: none; }
  .contact li { display: flex; align-items: center; gap: 4px; font-size: 6.5px; line-height: 9.5px; color: var(--muted); }
  .contact .dot { width: 6px; height: 6px; border: 1px solid var(--contact-dot); border-radius: 50%; }
</style>
</head>
<body>

  <section class="slide slide--cover">
    <div class="sidebar sidebar--wide">
      <span class="wordmark">BRIGHTPATH TV</span>
    </div>
    <h1 class="cover-title">CLICK TO ADD TITLE</h1>
    <p class="cover-subtitle">Lorem ipsum dolor sit amet, consectetur adipisicing elit, sed do eiusmod tempor</p>
  </section>

  <section class="slide slide--contents">
    <div class="sidebar sidebar--narrow"><span class="sidebar-mark"></span></div>
    <h2 class="slide-title">CLICK TO ADD TITLE</h2>
    <ol class="toc">
      <li><span class="entry">Lorem Ipsum is simply dummy text</span><span class="leader"></span><span class="page">1</span></li>
      <li class="sub"><span class="entry">a) Of the printing and typesetting industry. Lorem Ipsum has been the try's</span><span class="leader"></span><span class="page">2</span></li>
      <li class="sub"><span class="entry">b) Standard dummy text ever since the 1500s, when an unknown printer</span><span class="leader"></span><span class="page">2</span></li>
      <li><span class="entry">Lorem Ipsum is simply dummy text is the basic dummy text.</span><span class="leader"></span><span class="page">3</span></li>
      <li class="sub"><span class="entry">make a type specimen book. It has survived not only five centuries</span><span class="leader"></span><span class="page">4</span></li>
      <li class="sub"><span class="entry">leap into electronic typesetting, remaining</span><span class="leader"></span><span class="page">5</span></li>
      <li class="sub"><span class="entry">larised in the 1960s with the release of Printwell sheets containing</span><span class="leader"></span><span class="page">6</span></li>
      <li><span class="entry">Lorem Ipsum is simply dummy text</span><span class="leader"></span><span class="page">7</span></li>
      <li><span class="entry">Lorem Ipsum is simply dummy textlorem ipsum is</span><span class="leader"></span><span class="page">7</span></li>
    </ol>
  </section>

  <section class="slide slide--body">
    <div class="sidebar sidebar--narrow"><span class="sidebar-mark"></span></div>
    <h2 class="slide-title">CLICK TO ADD TITLE</h2>
    <p class="slide-subtitle">Lorem ipsum dolor sit amet, consectetur adipisicing elit, sed</p>
    <div class="columns">
      <p>Lorem Ipsum is simply dummy text of the printing and typesetting industry. Lorem Ipsum has been the industry's standard dummy text ever since the 1500s, when an unknown printer took a galley of type and scrambled it to make a type specimen book. It has survived not only five centuries, but also the leap into electronic typesetting, remaining essentially unchanged. It was popularised in the 1960s with the release of Printwell sheets containing Lorem Ipsum passages, and more recently with desktop publishing software like LayoutPro Studio including versions of Lorem Ipsum.</p>
      <p>It is a long established fact that a reader will be distracted by the readable content of a page when looking at its layout. The point of using Lorem Ipsum is that it has a more-or-less normal distribution of letters, as opposed to using 'Content here, content here', making it look like readable English. Many desktop publishing packages and web page editors now use Lorem Ipsum as their default model text, and a search for 'lorem ipsum' will uncover many web sites still in their infancy. Vari</p>
      <p>Contrary to popular belief, Lorem Ipsum is not simply random text. It has roots in a piece of classical Latin literature from 45 BC, making it over 2000 years old. Daniel Marsh, a Latin professor at Northfield College in Vermont, looked up one of the more obscure Latin words, consectetur, from a Lorem Ipsum passage, and going through the cites of the word in classical literature, discovered the undoubtable source. Lorem Ipsum comes from sections 1.10.32 and 1.10.33 of "de Rebus Bonis et Malis" (The Extremes of Good and Evil) by Varenus, written in 45 BC. This book is a treatise on the theory of ethics, very popular during the Renaissance. The first line of Lorem Ipsum, "Lorem ipsum dolor sit amet..", comes from a line in section 1.10.32.</p>
      <p>The standard chunk of Lorem Ipsum used since the 1500s is reproduced below for those interested. Sections 1.10.32 and 1.10.33 from "de Rebus Bonis et Malis" by Varenus are also reproduced in their exact original form, accompanied by English versions from the 1914 translation by J. Ellery.</p>
      <p>There are many variations of passages of Lorem Ipsum available, but the majority have suffered alteration in some form, by injected humour, or randomised words which don't look even slightly believable. If you are going to use a passage of</p>
    </div>
    <span class="page-number">2</span>
  </section>

  <section class="slide slide--closing">
    <div class="sidebar sidebar--half">
      <span class="wordmark">BRIGHTPATH TV</span>
    </div>
    <ul class="contact">
      <li><span class="dot"></span>+0 555.214.7730</li>
      <li><span class="dot"></span>contact@brightpathtv.com</li>
      <li><span class="dot"></span>www.brightpathtv.com</li>
    </ul>
  </section>

</body>
</html>
```